Customs House descriptive business cards

We require a two-sided business card that has a simple yet elegant design. We want to be able to promote our services as a customs house. This card should include our logo, contact info and services offered with the logo being on one side and the contact info and services on the flip side

Target Market(s)

Importers / exporters to and from the Bahamas

Industry/Entity Type

Logistics

Contact Information for Business Card

The front side of the card could have the logo and the flip side should have the other relevant info

Font styles to use
Serif

Colors

Designer to choose colors to be used in the design.

Requirements
Must have
• (Harbourline Agents Ltd) Logo, address and contact info also services:
• import customs clearance, Delivery & HAndling services,Florida pickups, Export packing & Crating Services, export customs clearance, Consulting

```html
<!DOCTYPE html>
<html lang="en">
<head>
<meta charset="utf-8">
<title>Harbourline Agents Ltd – Business Card</title>
<link href="https://fonts.googleapis.com/css2?family=Cormorant+Garamond:wght@500;600&family=Roboto:wght@400&display=swap" rel="stylesheet">
<style>
  :root {
    --page-bg: #d9d6d2;
    --card-dark: #040507;
    --card-mid: #1b1c20;
    --brand-blue: #2a5bb0;
    --name-blue: #1d3f8c;
    --title-tan: #d6c9b0;
    --contact-text: #ddd2bd;
    --icon-blue: #1f4a9a;
    --divider: rgba(255,255,255,0.18);
    --band-deep: #0b2462;
    --band-bright: #1d58b8;
    --band-silver: #9a9ea6;
    --service-text: #e9e2d4;
    --dot-pink: #e05a8a;
  }
  * { margin: 0; padding: 0; box-sizing: border-box; }
  html, body {
    width: 1200px; height: 969px; overflow: hidden;
    background: var(--page-bg);
  }
  .card {
    position: absolute; left: 100px; top: 200px;
    width: 1000px; height: 569px;
    background: radial-gradient(ellipse at 45% 40%, var(--card-mid) 0%, #0d0e11 55%, var(--card-dark) 100%);
    box-shadow: 0 18px 40px rgba(0,0,0,0.35);
    overflow: hidden;
  }
  .brand {
    position: absolute; left: 60px; top: 110px; width: 370px;
    text-align: center;
    font-family: "Cormorant Garamond", serif; font-weight: 600;
    color: var(--brand-blue);
  }
  .brand-mark {
    width: 96px; height: 96px; margin: 0 auto 34px;
    border-radius: 50%; background: var(--brand-blue);
  }
  .brand-name { font-size: 50px; line-height: 1; letter-spacing: 1px; }
  .brand-sub { font-size: 24px; letter-spacing: 7px; margin-top: 12px; }
  .divider {
    position: absolute; left: 484px; top: 90px;
    width: 1px; height: 300px; background: var(--divider);
  }
  .contact { position: absolute; left: 534px; top: 88px; }
  .person-name {
    font-family: "Cormorant Garamond", serif; font-weight: 600;
    font-size: 38px; color: var(--name-blue); letter-spacing: 1px; line-height: 1;
  }
  .person-title {
    font-family: "Cormorant Garamond", serif; font-weight: 500;
    font-size: 25px; color: var(--title-tan); letter-spacing: 1px; margin-top: 4px;
  }
  .address {
    font-family: "Roboto", sans-serif; font-size: 23px; line-height: 30px;
    color: var(--contact-text); margin-top: 22px;
  }
  .contact-list { list-style: none; margin-top: 24px; }
  .contact-list li {
    display: flex; align-items: center; gap: 14px;
    font-family: "Roboto", sans-serif; font-size: 22px; line-height: 32px;
    color: var(--contact-text);
  }
  .contact-list svg { width: 18px; height: 18px; fill: var(--icon-blue); flex: none; }
  .services-band {
    position: absolute; left: 0; top: 425px; width: 100%; height: 111px;
    background: linear-gradient(90deg, var(--band-deep) 0%, var(--band-bright) 45%, #2b4f9a 70%, var(--band-silver) 100%);
  }
  .services {
    position: absolute; left: 0; top: 10px; width: 820px;
    text-align: center;
    font-family: "Roboto", sans-serif; font-size: 22px; line-height: 30px;
    color: var(--service-text);
  }
  .services .dot { color: var(--dot-pink); padding: 0 4px; }
  .band-mark {
    position: absolute; right: 78px; top: 20px;
    width: 70px; height: 70px; border-radius: 50%;
    background: rgba(220,224,230,0.55);
  }
</style>
</head>
<body>
  <div class="card">
    <div class="brand">
      <div class="brand-mark"></div>
      <div class="brand-name">HARBOURLINE</div>
      <div class="brand-sub">AGENTS LTD</div>
    </div>

    <div class="divider"></div>

    <div class="contact">
      <div class="person-name">DANIEL REYES</div>
      <div class="person-title">CEO/FOUNDER</div>
      <div class="address">4120 Seabreeze Road<br>Nassau, Bahamas 10221</div>
      <ul class="contact-list">
        <li>
          <svg viewBox="0 0 24 24"><path d="M6.6 10.8a15.1 15.1 0 0 0 6.6 6.6l2.2-2.2c.3-.3.7-.4 1-.2 1.1.4 2.3.6 3.6.6.6 0 1 .4 1 1V20c0 .6-.4 1-1 1A17 17 0 0 1 3 4c0-.6.4-1 1-1h3.5c.6 0 1 .4 1 1 0 1.3.2 2.5.6 3.6.1.3 0 .7-.2 1z"/></svg>
          242 555 0148
        </li>
        <li>
          <svg viewBox="0 0 24 24"><path d="M7 1h10a2 2 0 0 1 2 2v18a2 2 0 0 1-2 2H7a2 2 0 0 1-2-2V3a2 2 0 0 1 2-2zm0 3v14h10V4zm5 15.5a1 1 0 1 0 0 2 1 1 0 0 0 0-2z"/></svg>
          242 555 0193
        </li>
        <li>
          <svg viewBox="0 0 24 24"><path d="M2 5h20v14H2zm2 2v.5l8 5 8-5V7zm0 3v7h16v-7l-8 5z"/></svg>
          daniel@harbourlineagents.com
        </li>
        <li>
          <svg viewBox="0 0 24 24"><path d="M12 2a10 10 0 1 0 0 20 10 10 0 0 0 0-20zm-1 17.9A8 8 0 0 1 4.1 11H7c.1 2.9.9 5.7 2.3 8zm0-8.9h2v8c-1.2-2.2-1.9-4.9-2-8zm2-2h-2c.1-3.1.8-5.8 2-8zm1.7 10.9c1.4-2.3 2.2-5.1 2.3-7.9h2.9a8 8 0 0 1-5.2 7.9zM17 9c-.1-2.8-.9-5.6-2.3-7.9A8 8 0 0 1 19.9 9zM9.3 3.1C7.9 5.4 7.1 8.2 7 9H4.1a8 8 0 0 1 5.2-5.9z"/></svg>
          www.harbourlineagents.com
        </li>
      </ul>
    </div>

    <div class="services-band">
      <p class="services">
        Import customs clearance<span class="dot">•</span>Delivery &amp; Handling services<br>
        Florida pickups<span class="dot">•</span>Export packing &amp; Crating Services<br>
        Export customs clearance<span class="dot">•</span>Consulting
      </p>
      <div class="band-mark"></div>
    </div>
  </div>
</body>
</html>
```